Seriöser Briefkopf für Rechtsanwaltskanzlei
Zielgruppe
Rechtsanwaltskanzlei
Aufgabenstellung
Benötigt wird ein seriöser Briefkopf für eine Anwaltskanzlei. Er soll im Wesentlichen aus Typen bestehen, mit denen aber durchaus 'gespielt' werden soll (Groß- und Kleinschreibung, querstehend, angeschnitten o.Ä)
Folgender Inhalt muss untergebracht werden:
Rechtsanwaltskanzlei Kessenhagen
Rechtsanwalt Dipl.-Ing. Udo Kessenhagen
Rechtsanwalt Matthias Wendel
Der Briefkopf muss schwarz-weiß druckbar sein und beim Versenden per Fax müssen alle Daten gut lesbar bleiben (also keine Grautöne bei Tel-Nr. o.Ä.)
Der Briefkopf soll mit einem Drucker ausgedruckt werden, sodass keine Gestaltung bis zum Blattrand gehen darf.
Bitte keine Logos mit Paragrafen-Zeichen oder Justitia und nicht die Abkürzung RUK verwenden.
Keine - Einfach drauflos - Ich bin gespannt

```html
<!DOCTYPE html>
<html lang="de">
<head>
<meta charset="utf-8">
<title>Briefbogen Rechtsanwaltskanzlei Kessenhagen</title>
<link href="https://fonts.googleapis.com/css2?family=EB+Garamond:wght@400&family=Tinos:wght@400&display=swap" rel="stylesheet">
<style>
  :root {
    --ink: #000000;
    --rule: #333333;
    --paper: #ffffff;
  }
  html, body {
    margin: 0;
    padding: 0;
    width: 849px;
    height: 1200px;
    overflow: hidden;
    background: var(--paper);
  }
  .sheet {
    position: relative;
    width: 849px;
    height: 1200px;
    background: var(--paper);
    color: var(--ink);
    font-family: "Tinos", "Times New Roman", serif;
  }
  .frame { position: absolute; left: 0; top: 0; }

  .wordmark {
    position: absolute;
    right: 24px;
    top: 56px;
    text-align: right;
    font-family: "EB Garamond", Georgia, serif;
    font-weight: 400;
    color: var(--ink);
    line-height: 1;
  }
  .wordmark-kind { font-size: 17px; letter-spacing: 0.5px; }
  .wordmark-name { font-size: 27px; letter-spacing: 1.5px; margin-top: 3px; }

  .sidebar {
    position: absolute;
    left: 611px;
    top: 114px;
    font-family: "EB Garamond", Georgia, serif;
    font-size: 10px;
    line-height: 13.5px;
    letter-spacing: 0.2px;
  }
  .sidebar p { margin: 0; }
  .partners { margin-bottom: 28px !important; }
  .office { margin-bottom: 5px !important; }
  .contact { margin-bottom: 5px !important; }
  .contact .label { display: inline-block; width: 22px; }

  .return-line {
    position: absolute;
    left: 82px;
    top: 203px;
    font-size: 9.6px;
    white-space: nowrap;
  }
  .recipient {
    position: absolute;
    left: 82px;
    top: 232px;
    font-size: 16.5px;
    line-height: 21px;
  }
  .recipient p { margin: 0; }

  .letter-body {
    position: absolute;
    left: 82px;
    top: 435px;
    width: 690px;
    font-size: 15.2px;
    line-height: 20.7px;
    hyphens: auto;
  }
  .letter-body p { margin: 0 0 20.7px 0; }
  .letter-body p.continued { margin-top: -20.7px; }
</style>
</head>
<body>
<div class="sheet">
  <svg class="frame" width="849" height="1200" viewBox="0 0 849 1200" aria-hidden="true">
    <line x1="73" y1="109" x2="829" y2="109" stroke="var(--rule)" stroke-width="0.8"/>
    <line x1="829" y1="109" x2="829" y2="1183" stroke="var(--rule)" stroke-width="0.8"/>
    <line x1="611" y1="1183" x2="829" y2="1183" stroke="var(--rule)" stroke-width="0.8"/>
    <line class="fold-mark" x1="12" y1="429" x2="28" y2="429" stroke="var(--rule)" stroke-width="0.8"/>
    <line class="fold-mark" x1="12" y1="860" x2="28" y2="860" stroke="var(--rule)" stroke-width="0.8"/>
  </svg>

  <div class="wordmark">
    <div class="wordmark-kind">Rechtsanwaltskanzlei</div>
    <div class="wordmark-name">KESSENHAGEN</div>
  </div>

  <div class="sidebar">
    <p class="partners">Rechtsanwalt Dipl.-Ing. Udo Kessenhagen<br>Rechtsanwalt Matthias Wendel</p>
    <p class="office">Lindenhofstraße 7<br>04109 Leipzig</p>
    <p class="contact"><span class="label">Tel.</span>0341 55720-0<br><span class="label">Fax</span>0341 55720-46</p>
    <p class="web">mail@kessenhagen-kanzlei.de<br>www.kessenhagen-kanzlei.de</p>
  </div>

  <div class="return-line">Rechtsanwaltskanzlei Kessenhagen · Lindenhofstraße 7 · 04109 Leipzig</div>

  <div class="recipient">
    <p>Herr Harald Mustermann</p>
    <p>Musterstraße 123</p>
    <p>12345 Musterfelden</p>
  </div>

  <div class="letter-body">
    <p>Sehr geehrter Herr Mustermann</p>
    <p>Asperio cor maio dic tem velesti sapit earionsedit, volendest vel eicil eturiti strum, ea quatur sed que corendita adis dest, sunt aut pores eos raecae vit iliatur alitatem velitatum, omni ius nem nis et pos int ut quiatiscitat dolloreserum expliqu isinullaccus consequam, officiaectur abo. Lit lit que peritio. Nam earum quid quas erferiore natemque et ut resenda ndemqui corero temperibusae comnimossime cus venducitat incitiur alignis non reprati am eum faccat doluptae nonsenet verferatis nis sam, quia invelendebis ex eles perum sa qui con ratias conet quae. Nam cum sit et volectem quia di nimus.</p>
    <p>Um sus, cumet pre asitios simpel evendestion rem fugia aut alis et voluptatent rerion con nihillut labo. Sitin recaecto odissit ullessi de conem si aut velent verae latem eni simaio. Debita volest ad magnist lique num incide liquam reroriorro dolor repta volupta ererat laborem quam que aliquo occum inversp eliquam nobitatum quatem eat unt ipiduciendi nest, autas consedi cum faccabo. Lut officiandi sinum aut magnatum fuga. Odignatum re comnihi liquat.</p>
    <p class="continued">Piendis maiorum laccabo. Essiti sit, sequosam, optatio dolum rent velecuptas por sin etum, ut quae landelibusae velitatio intio conserrum et apicatur?</p>
    <p>Arum hillupta dolor abo. Lesto tem faccaborrum asimi, conseque proreperrum volori tet ut hil essitium remperit vendi dus eos es pratur, eaque nus, unt exerum sinveles volum quas aliqui repudi cum sunt es estemol uptati verum exerumq uuntis utem est quis volupta dempore non pellab ipient provid explic te conse molecti audande rferum et laccum sinctametur molorum et re il ium faccusam faccationet landae magnia quunt re laborerum aute di doluptas remporeped qui am quia con reperibea sin nus sam quasi officabo.</p>
    <p>Quiduntes dolest es eiusam dolorit iscitiuri nonseque solorio rercim rerchil et ium arum quam, similles et officiis molorescia volorep elitia que prorporum inci officto blaccab orumquis dolorit re sunt quo voluptae officti oresequae volorrum rerum endio.</p>
    <p>MfG</p>
  </div>
</div>
</body>
</html>
```